Melissa Tarnow Personal Business Card

I like orange. It's would better if my card have an orange background
Address: 4720 Halberd Lane #318
San Jose
California
US
Tel: 4085172946

Industry/Entity Type

Business

```html
<!DOCTYPE html>
<html lang="en">
<head>
<meta charset="utf-8">
<title>Melissa Tarnow – Business Card</title>
<link rel="stylesheet" href="https://fonts.googleapis.com/css2?family=Rokkitt:wght@500&family=Signika:wght@400&display=swap">
<style>
  :root {
    --orange-deep: #ff5700;
    --orange-mid: #ff6a00;
    --orange-light: #ff9200;
    --ink: #1c1c1c;
  }
  html, body {
    margin: 0;
    padding: 0;
    width: 1200px;
    height: 686px;
    overflow: hidden;
  }
  .card {
    position: relative;
    width: 1200px;
    height: 686px;
    background: linear-gradient(90deg, var(--orange-deep) 0%, var(--orange-deep) 30%, var(--orange-mid) 45%, var(--orange-light) 85%, var(--orange-light) 100%);
    color: var(--ink);
    overflow: hidden;
  }
  .card__name {
    position: absolute;
    left: 64px;
    top: 196px;
    margin: 0;
    font-family: "Rokkitt", Georgia, serif;
    font-weight: 500;
    font-size: 84px;
    line-height: 1;
    letter-spacing: 0.5px;
  }
  .card__details {
    font-family: "Signika", "Trebuchet MS", sans-serif;
    font-size: 30px;
    line-height: 1;
  }
  .card__line {
    position: absolute;
    left: 67px;
    margin: 0;
    white-space: nowrap;
  }
  .card__line--street { top: 384px; }
  .card__line--city { top: 444px; left: 71px; }
  .card__line--region { top: 514px; }
  .card__line--phone { top: 579px; }
  .card__dash {
    display: inline-block;
    transform: translateY(-3px);
    margin: 0 2px;
  }
  .card__country {
    display: inline-block;
    transform: translateY(4px);
    letter-spacing: 4px;
  }
</style>
</head>
<body>
  <main class="card">
    <h1 class="card__name">Melissa Tarnow</h1>
    <address class="card__details" style="font-style: normal;">
      <p class="card__line card__line--street">4720 Halberd Lane #318</p>
      <p class="card__line card__line--city">San Jose</p>
      <p class="card__line card__line--region">California<span class="card__dash">–</span><span class="card__country">US</span></p>
      <p class="card__line card__line--phone">4085172946</p>
    </address>
  </main>
</body>
</html>
```